PNR Name Badge & Kiosk Stand Wrap

We are needing a name badge, ipad wrape, and stands created. These should be sent in AI, EPS and PDF format. The design guidlaines for the ipad stands are attached. We would like it to match our general overall themeing for Power NorthRidge. Do not mention a year or location so we can use it for future years.

```html
<!DOCTYPE html>
<html lang="en">
<head>
<meta charset="utf-8">
<title>Power NorthRidge – Kiosk Stand Wrap</title>
<link href="https://fonts.googleapis.com/css2?family=Kaushan+Script&display=swap" rel="stylesheet">
<style>
  :root {
    --page: #ffffff;
    --bleed: #e7ecea;
    --keyline: #3a3a3a;
    --red: #f2022f;
    --scarlet: #f4261d;
    --orange: #f85d05;
    --amber: #fb9003;
    --gold: #fdb104;
    --ink-light: #ffffff;
  }
  html, body {
    margin: 0;
    padding: 0;
    width: 1200px;
    height: 1089px;
    overflow: hidden;
    background: var(--page);
  }
  .stand-wrap {
    display: block;
    width: 1200px;
    height: 1089px;
  }
  .bleed-edge { fill: var(--bleed); stroke: var(--bleed); stroke-width: 18; stroke-linejoin: round; }
  .wrap-face { fill: url(#brandGradient); fill-rule: evenodd; stroke: var(--keyline); stroke-width: 0.6; }
  .screen-opening { fill: var(--page); stroke: var(--bleed); stroke-width: 18; }
  .brand-script {
    font-family: "Kaushan Script", cursive;
    fill: var(--ink-light);
    text-anchor: middle;
  }
  .brand-script--side { font-size: 50px; }
  .brand-script--base { font-size: 52px; }
  .brand-mark {
    font-family: "Kaushan Script", cursive;
    fill: var(--ink-light);
    text-anchor: middle;
  }
  .brand-mark--top { font-size: 22px; }
  .brand-mark--small { font-size: 11px; }
  .brand-dot { fill: var(--ink-light); }
</style>
</head>
<body>
<svg class="stand-wrap" viewBox="0 0 1200 1089" xmlns="http://www.w3.org/2000/svg" aria-label="Power NorthRidge tablet kiosk stand wrap">
  <defs>
    <linearGradient id="brandGradient" x1="0.3" y1="0.25" x2="0.65" y2="0.8">
      <stop offset="0" stop-color="var(--red)"/>
      <stop offset="0.35" stop-color="var(--scarlet)"/>
      <stop offset="0.55" stop-color="var(--orange)"/>
      <stop offset="0.72" stop-color="var(--amber)"/>
      <stop offset="0.85" stop-color="var(--gold)"/>
      <stop offset="1" stop-color="var(--gold)"/>
    </linearGradient>
    <path id="outerShape" d="M220,209 Q620,155 990,209 Q1060,215 1075,285 L1075,358 L1082,358 L1082,734 L1075,734 L1075,808 Q1068,875 990,880 Q620,950 220,880 Q140,875 132,808 L132,736 L126,732 L126,358 Q132,355 132,348 L132,285 Q140,215 220,209 Z"/>
    <path id="screenShape" d="M235,281 L298,281 Q306,281 309,273 Q313,262 320,262 Q328,262 331,273 Q334,281 342,281 L563,281 Q572,281 575,274 L583,262 Q588,259 595,259 L650,259 Q657,259 662,265 L669,276 Q672,281 680,281 L966,281 Q975,281 975,290 L975,799 Q975,808 966,808 L236,808 Q227,808 227,799 L227,290 Q227,281 235,281 Z"/>
    <clipPath id="screenClip"><use href="#screenShape"/></clipPath>
  </defs>

  <use class="bleed-edge" href="#outerShape"/>

  <path class="wrap-face" d="M220,209 Q620,155 990,209 Q1060,215 1075,285 L1075,358 L1082,358 L1082,734 L1075,734 L1075,808 Q1068,875 990,880 Q620,950 220,880 Q140,875 132,808 L132,736 L126,732 L126,358 Q132,355 132,348 L132,285 Q140,215 220,209 Z M235,281 L298,281 Q306,281 309,273 Q313,262 320,262 Q328,262 331,273 Q334,281 342,281 L563,281 Q572,281 575,274 L583,262 Q588,259 595,259 L650,259 Q657,259 662,265 L669,276 Q672,281 680,281 L966,281 Q975,281 975,290 L975,799 Q975,808 966,808 L236,808 Q227,808 227,799 L227,290 Q227,281 235,281 Z"/>

  <use class="screen-opening" href="#screenShape" clip-path="url(#screenClip)"/>

  <g class="brand-top">
    <circle class="brand-dot" cx="588" cy="232" r="5"/>
    <text class="brand-mark brand-mark--top" x="622" y="240">PNR</text>
  </g>

  <text class="brand-script brand-script--side" transform="translate(188 545) rotate(-90)">Power NorthRidge</text>
  <text class="brand-script brand-script--side" transform="translate(1018 545) rotate(90)">Power NorthRidge</text>
  <text class="brand-script brand-script--base" x="600" y="875">Power NorthRidge</text>

  <text class="brand-mark brand-mark--small" x="826" y="876">PNR</text>
</svg>
</body>
</html>
```